Newsletter Design Project for electrical maintenance company

1.We need a monthly newsletter tempate designed in mail chimp.
2. We will provide the basic information for the newsletter
3. you will edit and copy write newsletter
We would love this to be an on going monthly partnership
For now, design template and do 1 newsletter
Its a light hearted news letter
40% relavent info. e.g. talk about smoke alarms
Personal information about what we are up to - family etc
update on workers - whos new, perosnal profiles etc
each newsletter to have a specific product special
e.g. $50 off second smoke alarm
Each news letter to contain 5 energy saving tips
www.brightlanehelpers.com.au for more company info
residiential home owners - Mainly females
Electrical

```html
<!DOCTYPE html>
<html lang="en">
<head>
<meta charset="utf-8">
<title>Bright Lane Helpers – June 2013 Newsletter</title>
<link rel="stylesheet" href="https://fonts.googleapis.com/css2?family=Oswald:wght@500;700&family=Arimo:wght@400;700&display=swap">
<style>
  :root {
    --page-blue: #0465a9;
    --teal: #27a5c1;
    --orange: #f7931e;
    --charcoal: #333236;
    --white: #ffffff;
    --ink: #1a1a1a;
    --display: "Oswald", "Arial Narrow", sans-serif;
    --body: "Arimo", Arial, sans-serif;
  }
  * { box-sizing: border-box; margin: 0; padding: 0; }
  html, body { width: 1200px; height: 837px; overflow: hidden; }
  body { background: var(--page-blue); font-family: var(--body); color: var(--ink); position: relative; }
  .abs { position: absolute; }

  .browser-note { left: 347px; top: 6px; font-size: 8.5px; color: #0a1a2a; }

  .issue-date { left: 347px; top: 21px; width: 227px; height: 41px; background: var(--charcoal);
    color: var(--white); font-family: var(--display); font-weight: 500; font-size: 25px;
    display: flex; align-items: center; justify-content: center; gap: 5px; letter-spacing: 0.5px; }
  .call-bar { left: 574px; top: 28px; width: 279px; height: 28px; background: var(--teal);
    color: var(--white); font-family: var(--display); font-weight: 700; font-size: 21px;
    line-height: 28px; padding-left: 13px; letter-spacing: -0.3px; }

  .panel { background: var(--white); }
  .hero { left: 347px; top: 62px; width: 506px; height: 202px; }
  .brand-mark { left: 30px; top: 40px; width: 160px; height: 120px; border-radius: 8px;
    background: radial-gradient(circle at 50% 45%, #f3c9a0 0%, #e8eef2 70%);
    display: flex; align-items: flex-end; justify-content: center; padding-bottom: 8px; }
  .brand-name { font-family: var(--body); font-weight: 700; font-size: 13px; color: var(--orange); }
  .hero-heading { left: 220px; top: 18px; width: 270px; font-size: 11.4px; font-weight: 700;
    color: var(--teal); line-height: 17.6px; text-transform: uppercase; }
  .copy { font-size: 12px; line-height: 15.2px; color: var(--ink); }
  .hero-copy { left: 220px; top: 86px; width: 272px; }
  .more { width: 23px; height: 23px; }

  .tab-dark { background: var(--charcoal); color: var(--white); font-family: var(--display);
    font-weight: 700; font-size: 22px; line-height: 37px; padding-left: 9px; letter-spacing: -0.5px; }
  .tab-bar { color: var(--white); font-family: var(--display); font-weight: 700; font-size: 21px;
    line-height: 24px; padding-left: 9px; letter-spacing: -0.3px; }

  .news { left: 347px; top: 311px; width: 248px; height: 288px; }
  .news-date { font-size: 12px; font-weight: 700; color: var(--orange); left: 13px; }
  .thumb { left: 13px; width: 79px; height: 78px; }
  .news-copy { left: 105px; width: 135px; font-size: 12px; line-height: 14.4px; }
  .divider { left: 0; top: 143px; width: 248px; border-top: 1px dashed #e3e3e3; }

  .events { left: 605px; top: 311px; width: 248px; height: 288px; }
  .big-figure { left: 16px; top: 10px; font-family: var(--display); font-weight: 700; font-size: 72px;
    line-height: 72px; color: var(--teal); letter-spacing: 1px; }
  .events-heading { left: 17px; top: 92px; width: 225px; font-size: 11.4px; font-weight: 700;
    color: var(--teal); line-height: 17.6px; text-transform: uppercase; }
  .events-copy { left: 17px; top: 141px; width: 212px; }

  .promo { top: 611px; width: 248px; height: 161px; }
  .promo-image { left: 0; top: 0; width: 248px; height: 124px; }
  .promo-bar { left: 0; top: 124px; width: 248px; height: 37px; background: var(--orange);
    color: var(--white); font-family: var(--display); font-weight: 700; font-size: 22px;
    line-height: 37px; padding-left: 13px; letter-spacing: -0.3px; }

  .footer { left: 347px; top: 783px; width: 506px; height: 41px; background: var(--teal); }
  .social { top: 8px; width: 25px; height: 25px; border-radius: 5px; background: var(--white); }
  .footer-note { left: 158px; top: 11px; font-size: 8.4px; line-height: 12px; color: var(--white); }
</style>
</head>
<body>
  <p class="abs browser-note">Email not displaying properly? View it in your browser</p>

  <div class="abs issue-date">
    <span>JUNE</span>
    <svg width="31" height="27" viewBox="0 0 31 27" aria-hidden="true">
      <rect x="1" y="1" width="29" height="25" rx="6" fill="#fff"/>
      <rect x="6" y="7" width="19" height="13" fill="none" stroke="#333236" stroke-width="1.8"/>
      <path d="M6 7 L15.5 15 L25 7 M6 20 L12.5 13.5 M25 20 L18.5 13.5" fill="none" stroke="#333236" stroke-width="1.6"/>
    </svg>
    <span>2013</span>
  </div>
  <div class="abs call-bar">CALL US NOW: 1300 555 014</div>

  <section class="abs panel hero">
    <div class="abs brand-mark" role="img" aria-label="Company mascot illustration: caped hero holding a light bulb">
      <span class="brand-name">Bright Lane Helpers</span>
    </div>
    <h2 class="abs hero-heading">Amet consectetuer adipiscing elit, sed diam nonummy nibh euismod tinci diam laoreet dolore magna aliquam erat</h2>
    <p class="abs copy hero-copy">Lorem ipsum dolor sit amet elit, consectetur et adipiscing elit. Aenean eget et sem mauris, et facilisis odio. Fusce pellentesque nulla ac diam felis cursus adipscing lacus feugiat. Proin sit amet elit in quam dapibus.</p>
    <svg class="abs more" style="left:465px;top:163px" viewBox="0 0 23 23" aria-hidden="true"><circle cx="11.5" cy="11.5" r="11.5" fill="#333236"/><path d="M11.5 5.5v12M5.5 11.5h12" stroke="#fff" stroke-width="3"/></svg>
  </section>

  <div class="abs tab-dark" style="left:347px;top:274px;width:86px;height:37px">LATEST</div>
  <div class="abs tab-bar" style="left:433px;top:281px;width:162px;height:24px;background:var(--teal)">NEWS</div>
  <div class="abs tab-dark" style="left:605px;top:274px;width:86px;height:37px">WHAT'S</div>
  <div class="abs tab-bar" style="left:691px;top:281px;width:162px;height:24px;background:var(--orange)">GOING ON</div>

  <section class="abs panel news">
    <p class="abs news-date" style="top:15px">TUESDAY, JAN 20, 2013</p>
    <div class="abs thumb" style="top:35px;background:linear-gradient(135deg,#e9e3dc,#6b4a3a 55%,#1e2a44)" role="img" aria-label="Photo of a woman using a mobile phone"></div>
    <p class="abs news-copy" style="top:36px">Etiam eros massa, porta sed eros viva et semper eget, consectetur sed et semper a mi. Vivamus in vehicula erat.</p>
    <svg class="abs more" style="left:212px;top:118px" viewBox="0 0 23 23" aria-hidden="true"><circle cx="11.5" cy="11.5" r="11.5" fill="#333236"/><path d="M11.5 5.5v12M5.5 11.5h12" stroke="#fff" stroke-width="3"/></svg>
    <div class="abs divider"></div>
    <p class="abs news-date" style="top:166px">FRIDAY, MAR 20, 2013</p>
    <div class="abs thumb" style="top:186px;background:linear-gradient(135deg,#1f6fb4,#7fb7de 45%,#c9b9a4 75%,#8a7d6e)" role="img" aria-label="Photo of an open hard disk drive on a digital background"></div>
    <p class="abs news-copy" style="top:187px">Etiam eros massa, porta sed eros viva et semper eget, consectetur sed et semper a mi. Vivamus in vehicula erat.</p>
    <svg class="abs more" style="left:212px;top:256px" viewBox="0 0 23 23" aria-hidden="true"><circle cx="11.5" cy="11.5" r="11.5" fill="#333236"/><path d="M11.5 5.5v12M5.5 11.5h12" stroke="#fff" stroke-width="3"/></svg>
  </section>

  <section class="abs panel events">
    <p class="abs big-figure">15M/A</p>
    <h2 class="abs events-heading">Nulla consectetuer adipiscing sed diam nonummy nib euismod</h2>
    <p class="abs copy events-copy">Lorem ipsum ipsum dolor sit amet elit, consectetur et adipiscing elit. Aenean eget sit sem mauris, et facilisis odio. Fusce pellentesque nulla ac diam felis cursus eu dia adipiscing lacus feugiat. Proin sit amet elit in quam dapibus. Vivamus ac in vehicula erat. Proin sit amet elit in quam dapibus.</p>
    <svg class="abs more" style="left:213px;top:256px" viewBox="0 0 23 23" aria-hidden="true"><circle cx="11.5" cy="11.5" r="11.5" fill="#333236"/><path d="M11.5 5.5v12M5.5 11.5h12" stroke="#fff" stroke-width="3"/></svg>
  </section>

  <section class="abs promo" style="left:347px">
    <div class="abs promo-image" style="background:linear-gradient(180deg,#ffffff 0%,#f1f1f1 55%,#d9d9d9 100%)" role="img" aria-label="Photo of a laptop, tablet, monitor and phone"></div>
    <div class="abs promo-bar">SPECIAL</div>
    <svg class="abs more" style="left:213px;top:131px" viewBox="0 0 23 23" aria-hidden="true"><circle cx="11.5" cy="11.5" r="11.5" fill="#fff"/><path d="M11.5 5.5v12M5.5 11.5h12" stroke="#f7931e" stroke-width="3"/></svg>
  </section>
  <section class="abs promo" style="left:605px">
    <div class="abs promo-image" style="background:linear-gradient(160deg,#f4f4f4 0%,#dcdcdc 40%,#c9b79a 60%,#1a1a1a 80%)" role="img" aria-label="Close-up photo of a white tablet corner with camera"></div>
    <div class="abs promo-bar">CHECK THIS OUT</div>
    <svg class="abs more" style="left:213px;top:131px" viewBox="0 0 23 23" aria-hidden="true"><circle cx="11.5" cy="11.5" r="11.5" fill="#fff"/><path d="M11.5 5.5v12M5.5 11.5h12" stroke="#f7931e" stroke-width="3"/></svg>
  </section>

  <footer class="abs footer">
    <span class="abs social" style="left:10px"></span>
    <span class="abs social" style="left:47px"></span>
    <svg class="abs" style="left:81px;top:8px" width="25" height="25" viewBox="0 0 25 25" aria-label="Email">
      <rect width="25" height="25" rx="5" fill="#fff"/>
      <rect x="5" y="7.5" width="15" height="10" fill="none" stroke="#27a5c1" stroke-width="1.6"/>
      <path d="M5 7.5 L12.5 13.5 L20 7.5" fill="none" stroke="#27a5c1" stroke-width="1.6"/>
    </svg>
    <span class="abs social" style="left:118px"></span>
    <p class="abs footer-note">You have received this email cause you have subscribed to hello@brightlanehelpers.com.au.<br>If you no longer wish to receive emails please unsubscribe; © 2013 Your Company</p>
  </footer>
</body>
</html>
```